Patient Recruitment Presentation for a Clinical Trial

We need a powerpoint designed to recruit patients for a clinical trial. We need 4 slides designed: an opening slide, two body slides, and an end slide. The opening slide should include the question, "Do you suffer from Depression?" in the middle of the screen, but other than that just include the design, graphic, or texture that you develop. The 2 body slides should allow for the title of study (please use “Depression Research Study”) to be across the top and contact information (phone number, URL) to be on the bottom of the slide, either centered or left or right justified. Whether this text (study title and contact information) is set off by a banner or shape that stretches across the entire slide or just provides a background to that text is up to you. One of the two body slides should include the attached horizontal stock image with a clear section to insert text either beside or over the top of the negative space of the image. This image should be stretch to the full width of the screen. The second body slide should include the attached vertical stock image, with a clear section to insert text beside the picture. (You can crop vertical portions of the images if needed.)

The end slide should resemble the opening slide in terms of design, yet this time includes the study title and contact information prominently displayed.

In terms of design, we’re looking for something clean and trustworthy, and even though this is medical, we don’t want any pills, test tubes, or heart rate lines. We’re trying to give people hope, so we want to earn their trust by communicating quality and excellence.

Please see the attached examples of the types of designs and layouts we like, how the images need to be treated, and places for text need to be designed.

We need the design to be 1920x1080 pixels, and we need the slides delivered as layered PSD files so we can manipulate as needed.

Thanks!

Target Market(s)

Adults in the US that are not working full time and able to participate in a research study.

Industry/Entity Type

Medical

Font styles to use
Serif
Sans Serif

Requirements
Must have
• The design must use the two images attached as specified in the brief. Other than that, I'm open to your creative interpretation.
Nice to have
• Nice clean design, clean fonts, nice color palette.
Should not have
• Images or designs relating to the medical world, no test tubes, heart rate lines, images of doctors or pills, etc.

```html
<!DOCTYPE html>
<html lang="en">
<head>
<meta charset="utf-8">
<title>Depression Research Study</title>
<link href="https://fonts.googleapis.com/css2?family=Roboto+Condensed:wght@400;700&display=swap" rel="stylesheet">
<style>
  :root {
    --bg-light: #f4f4f5;
    --bg-mid: #e6e7e9;
    --brand-blue: #1f6ea8;
    --bar-blue-top: #2f93c8;
    --bar-blue-bottom: #176b9e;
    --ink: #111111;
    --white: #ffffff;
    --edge-grey: #d4d6d9;
    --photo-dark: #3a2a22;
    --photo-mid: #8a6350;
    --photo-light: #c9b2a4;
    --photo-shirt: #b9c7d3;
  }
  html, body { margin: 0; padding: 0; overflow: hidden; }
  body { width: 1200px; height: 675px; }
  .slide {
    position: relative;
    width: 1200px;
    height: 675px;
    overflow: hidden;
    background: linear-gradient(135deg, var(--bg-light) 0%, var(--bg-mid) 100%);
    font-family: "Roboto Condensed", "Arial Narrow", sans-serif;
  }
  .shapes { position: absolute; inset: 0; }
  .study-badge {
    position: absolute;
    left: 970px;
    top: 20px;
    width: 220px;
    transform: rotate(-16deg);
    transform-origin: center;
    color: var(--brand-blue);
    font-weight: 700;
    font-size: 40px;
    line-height: 52px;
    text-align: center;
    margin: 0;
  }
  .symptoms { position: absolute; left: 640px; top: 238px; margin: 0; }
  .symptoms-heading {
    margin: 0 0 4px;
    font-weight: 700;
    font-size: 28px;
    line-height: 34px;
    color: var(--ink);
  }
  .symptom-list { list-style: none; margin: 0; padding: 0 0 0 30px; }
  .symptom-list li {
    display: flex;
    align-items: center;
    height: 42px;
    font-size: 27px;
    color: var(--brand-blue);
  }
  .tick-box { width: 21px; height: 21px; margin-right: 10px; flex: none; }
  .contact-phone {
    position: absolute;
    left: 56px;
    top: 562px;
    margin: 0;
    font-size: 60px;
    line-height: 70px;
    font-weight: 400;
    color: var(--brand-blue);
  }
  .contact-email {
    position: absolute;
    right: 90px;
    top: 620px;
    margin: 0;
    font-size: 30px;
    line-height: 40px;
    color: var(--white);
  }
</style>
</head>
<body>
<main class="slide">
  <svg class="shapes" width="1200" height="675" viewBox="0 0 1200 675">
    <defs>
      <linearGradient id="photoTone" x1="0" y1="0" x2="1" y2="1">
        <stop offset="0" stop-color="var(--photo-dark)"/>
        <stop offset="0.45" stop-color="var(--photo-mid)"/>
        <stop offset="0.8" stop-color="var(--photo-light)"/>
        <stop offset="1" stop-color="var(--photo-shirt)"/>
      </linearGradient>
      <linearGradient id="barBlue" x1="0" y1="0" x2="0" y2="1">
        <stop offset="0" stop-color="var(--bar-blue-top)"/>
        <stop offset="1" stop-color="var(--bar-blue-bottom)"/>
      </linearGradient>
    </defs>

    <polygon class="photo-area" role="img" aria-label="Photo of a thoughtful woman resting her fingertips on her temple"
      fill="url(#photoTone)"
      points="0,0 150,0 175,10 440,85 610,125 525,375 560,560 0,560"/>

    <polygon class="badge-tab" points="960,0 1200,0 1200,225 1120,225 955,165 935,40"
      fill="var(--white)" stroke="var(--edge-grey)" stroke-width="1"/>

    <polygon class="contact-band" points="0,548 555,548 600,605 690,605 640,640 0,640" fill="var(--white)"/>
    <polygon class="email-bar" points="690,605 1200,605 1200,675 0,675 0,640 640,640" fill="url(#barBlue)"/>
    <polygon class="band-accent" points="555,548 600,605 585,610" fill="#d9dbde"/>
  </svg>

  <h1 class="study-badge">Depression Research Study</h1>

  <section class="symptoms">
    <h2 class="symptoms-heading">Signs and symptoms of depression include :</h2>
    <ul class="symptom-list">
      <li><svg class="tick-box" viewBox="0 0 20 20"><rect x="1" y="1" width="18" height="18" fill="none" stroke="var(--brand-blue)" stroke-width="2"/><polyline points="4,10 8,14 16,5" fill="none" stroke="var(--brand-blue)" stroke-width="2.5"/></svg>Feelings of helplessness and hopelessness</li>
      <li><svg class="tick-box" viewBox="0 0 20 20"><rect x="1" y="1" width="18" height="18" fill="none" stroke="var(--brand-blue)" stroke-width="2"/><polyline points="4,10 8,14 16,5" fill="none" stroke="var(--brand-blue)" stroke-width="2.5"/></svg>Loss of interest in daily activities.</li>
      <li><svg class="tick-box" viewBox="0 0 20 20"><rect x="1" y="1" width="18" height="18" fill="none" stroke="var(--brand-blue)" stroke-width="2"/><polyline points="4,10 8,14 16,5" fill="none" stroke="var(--brand-blue)" stroke-width="2.5"/></svg>Appetite or weight changes</li>
      <li><svg class="tick-box" viewBox="0 0 20 20"><rect x="1" y="1" width="18" height="18" fill="none" stroke="var(--brand-blue)" stroke-width="2"/><polyline points="4,10 8,14 16,5" fill="none" stroke="var(--brand-blue)" stroke-width="2.5"/></svg>Sleep changes</li>
      <li><svg class="tick-box" viewBox="0 0 20 20"><rect x="1" y="1" width="18" height="18" fill="none" stroke="var(--brand-blue)" stroke-width="2"/><polyline points="4,10 8,14 16,5" fill="none" stroke="var(--brand-blue)" stroke-width="2.5"/></svg>Anger or irritability</li>
      <li><svg class="tick-box" viewBox="0 0 20 20"><rect x="1" y="1" width="18" height="18" fill="none" stroke="var(--brand-blue)" stroke-width="2"/><polyline points="4,10 8,14 16,5" fill="none" stroke="var(--brand-blue)" stroke-width="2.5"/></svg>Self-loathing</li>
      <li><svg class="tick-box" viewBox="0 0 20 20"><rect x="1" y="1" width="18" height="18" fill="none" stroke="var(--brand-blue)" stroke-width="2"/><polyline points="4,10 8,14 16,5" fill="none" stroke="var(--brand-blue)" stroke-width="2.5"/></svg>Reckless behavior</li>
    </ul>
  </section>

  <p class="contact-phone">1-823-555-0147</p>
  <p class="contact-email">contact@mindwellstudy.org</p>
</main>
</body>
</html>
```